Update patient consent forms and contract

Objective
Redesign the existing patient contract information document to create a modern,contempory, and easy-to-understand experience for patients. The updated design should improve readability, accessibility, and overall presentation while maintaining compliance with healthcare and legal requirements.

Key Deliverables

Refreshed visual design and layout
Improved information hierarchy and readability
Modern typography and colour palette aligned with brand guidelines
Clear section headings and navigation
Print-ready and digital versions (PDF)

Include KVE Logo within patient KVE consent to treatment. Ideally this document should be portrait not landscape.
Updates

I would love a front page to be included in the document

```html
<!DOCTYPE html>
<html lang="en">
<head>
<meta charset="utf-8">
<title>Patient Information &amp; Consent Pack – Page Spreads</title>
<link href="https://fonts.googleapis.com/css2?family=Noto+Sans:wght@400;600;700&display=swap" rel="stylesheet">
<style>
:root{
  --bg:#dcdcdc;
  --paper:#ffffff;
  --cover-paper:#f3fbfd;
  --navy:#0f3447;
  --navy-2:#1a4658;
  --teal:#15a3c6;
  --cyan:#58d2e6;
  --cyan-soft:#b7eef5;
  --tint:#eef8fb;
  --tint-2:#e1f4f8;
  --line:#cfdde3;
  --ink:#1c2e38;
  --muted:#7c8e97;
  --amber:#efb54b;
  --amber-tint:#fdf5e4;
}
*{box-sizing:border-box;margin:0;padding:0}
html,body{width:1200px;height:927px;overflow:hidden;background:var(--bg)}
body{font-family:"Noto Sans",Arial,sans-serif;color:var(--ink)}
.stage{position:absolute;left:0;top:0;width:2184px;height:1688px;transform:scale(0.54945);transform-origin:0 0}
.page{position:absolute;width:395px;height:557px;background:var(--paper);box-shadow:0 3px 8px rgba(0,0,0,.35);overflow:hidden}
.band{position:absolute;left:0;top:0;bottom:0;width:7px;background:var(--teal)}
.band::after{content:"";position:absolute;left:7px;top:0;bottom:0;width:6px;background:var(--tint)}
.brand{position:absolute;left:43px;top:19px;display:flex;align-items:center;gap:3px;font-size:10px;font-weight:600;color:#5f7883}
.brand i{display:block;width:7px;height:7px;border-radius:50%;background:var(--teal)}
.pack-label{position:absolute;right:38px;top:19px;font-size:4px;color:var(--muted)}
.rule{position:absolute;left:43px;right:38px;top:33px;border-top:.6px solid var(--line)}
.foot{position:absolute;left:43px;right:38px;top:531px;display:flex;justify-content:space-between;font-size:3.6px;color:var(--muted)}
.abs{position:absolute}
.title-card{position:absolute;left:47px;right:42px;top:65px;height:47px;background:var(--tint);border-left:3px solid var(--teal);padding:7px 9px}
.eyebrow{font-size:3.8px;font-weight:700;color:var(--teal);letter-spacing:.2px;text-transform:uppercase}
.title{font-size:11px;font-weight:700;color:var(--navy);margin-top:1px}
.subtitle{font-size:4.2px;color:var(--muted);margin-top:3px}
.card{position:absolute;background:#fff;border:.6px solid var(--line);border-radius:3px;padding:6px 7px;font-size:4.4px;line-height:1.32;color:var(--ink)}
.card.bar{border-left:2.5px solid var(--teal)}
.card.tint{background:var(--tint)}
.card.teal-note{background:var(--tint-2);border-color:#c4e7ef}
.card.amber{background:var(--amber-tint);border-left:2.5px solid var(--amber);border-color:#f1ddb2}
.card h4{font-size:4.8px;font-weight:700;color:var(--navy);margin-bottom:1.5px}
.card p{margin-bottom:1.5px}
.lead{position:absolute;font-size:5.2px;line-height:1.35;color:var(--ink)}
.risk{padding:5px 6px 5px 25px}
.risk .num{position:absolute;left:5px;top:6px;width:11px;height:11px;border:.7px solid var(--teal);border-radius:50%;font-size:3.6px;font-weight:700;color:var(--teal);display:flex;align-items:center;justify-content:center}
.risk h4{margin-top:6px}
.risk p{font-size:3.6px;line-height:1.3}
.fields{display:grid;grid-template-columns:1fr 1fr;gap:5px 10px}
.field{font-size:3.8px;color:var(--muted);border-bottom:.6px solid var(--line);padding:4px 0 5px}
.mark{display:flex;align-items:center;gap:5px;font-size:11px;font-weight:600;color:#5f7883}
.mark i{display:block;width:26px;height:26px;border-radius:50%;background:#cdd8dd}
.check{display:flex;gap:5px;align-items:center;font-size:4.6px;margin-bottom:5px}
.box{width:5px;height:5px;border:.7px solid var(--teal);flex:none}
table.bank{width:100%;font-size:4px;border-collapse:collapse}
table.bank td{padding:2.4px 4px;border-bottom:.5px solid var(--line)}
/* cover */
.cover{background:var(--cover-paper)}
.cover-panel{position:absolute;left:52px;top:51px;width:289px;height:455px;background:var(--navy);border-radius:10px;overflow:hidden}
.cover-head{position:absolute;left:0;top:0;right:0;height:174px;background:var(--teal)}
.cover-logo{position:absolute;left:26px;top:6px;width:120px;height:44px;background:#fff;border-radius:3px;display:flex;align-items:center;padding-left:10px}
.cover-title{position:absolute;left:86px;top:172px;font-size:17px;font-weight:700;line-height:1.4;color:#fff}
.cover-sub{position:absolute;left:88px;top:231px;font-size:6px;color:#e4f3f7}
.prepared{position:absolute;left:86px;top:291px;width:221px;height:104px;background:#fff;border-radius:4px;padding:20px 14px}
.prepared b{font-size:6px;color:var(--navy)}
.prepared .ln{border-bottom:.6px solid var(--line);margin-top:18px}
.prepared small{display:block;font-size:3.8px;color:var(--muted);margin-top:3px}
.includes{position:absolute;left:86px;top:418px;width:221px;height:52px;background:var(--navy-2);border-radius:4px;padding:13px 14px;color:#fff}
.includes b{font-size:4.8px}
.includes small{display:block;font-size:3.6px;color:#b8cdd6;margin-top:7px}
</style>
</head>
<body>
<div class="stage">

<!-- Page 1: cover -->
<section class="page cover" style="left:22px;top:199px">
  <div class="cover-panel">
    <div class="cover-head"></div>
    <div class="cover-logo"><span class="brand" style="position:static"><i></i>harbourline</span></div>
    <svg class="abs" style="left:0;top:0" width="289" height="455" viewBox="0 0 289 455">
      <circle cx="286" cy="62" r="115" fill="var(--cyan)"/>
      <circle cx="306" cy="118" r="70" fill="var(--cyan-soft)"/>
      <path d="M170 190 Q230 225 300 170" fill="none" stroke="#8ad9e7" stroke-width="1"/>
      <path d="M160 200 Q235 245 305 185" fill="none" stroke="#6bb8c9" stroke-width=".7"/>
    </svg>
    <div class="abs" style="left:0;top:174px;right:0;height:281px;background:var(--navy)"></div>
  </div>
  <div class="cover-title">Patient Information<br>&amp; Consent Pack</div>
  <div class="cover-sub">Orthodontic Treatment | Payment Options | Retainer Policy</div>
  <div class="prepared">
    <b>Prepared for</b>
    <div class="ln"></div><small>Patient name</small>
    <div style="display:flex;gap:14px;align-items:baseline;margin-top:6px"><b>Date</b><small>DD / MM / YYYY</small></div>
  </div>
  <div class="includes">
    <b>Includes KVE Society of Orthodontists consent to treatment</b>
    <small>Designed as a clear, portrait-format patient pack for print and digital use.</small>
  </div>
  <div class="abs" style="left:78px;top:490px;font-size:3.6px;color:#b8cdd6">© Harbourline Orthodontics | Registered Specialist Orthodontists</div>
</section>

<!-- Page 2: welcome -->
<section class="page" style="left:459px;top:199px">
  <div class="band"></div>
  <div class="brand"><i></i>harbourline</div><div class="pack-label">Patient Information &amp; Consent Pack</div><div class="rule"></div>
  <div class="title-card"><div class="eyebrow">Patient pack</div><div class="title">Welcome &amp; document guide</div><div class="subtitle">Please review each section carefully before signing.</div></div>
  <p class="lead" style="left:47px;right:42px;top:118px">This redesigned pack organizes the patient information into clear, accessible sections while keeping the consent, payment and retainer policy content in a professional document format.</p>
  <div class="card bar" style="left:47px;top:142px;width:145px;height:56px"><h4>01 KVE Consent to Treatment</h4><p>Orthodontic treatment overview, benefits, material risks and final consent signature area.</p></div>
  <div class="card bar" style="left:200px;top:142px;width:147px;height:56px"><h4>02 Payment Option Selection</h4><p>Patient payment method selection, direct debit information, transfer reference guidance and bank details.</p></div>
  <div class="card bar" style="left:47px;top:205px;width:145px;height:56px"><h4>03 Retainer Policy</h4><p>Retainer guidance, removable retainer policy, bonded retainer explanation and follow-up information.</p></div>
  <div class="card bar" style="left:200px;top:205px;width:147px;height:56px"><h4>04 Patient Completion</h4><p>Patient name, date and required signatures are clearly separated for easier completion.</p></div>
  <div class="card teal-note" style="left:47px;top:272px;width:305px;height:44px;font-size:4.3px;color:#45606c">Design note: this version uses an editorial healthcare layout with a strong cover, section cards, left-page accent band, clear risk cards and generous signature spaces. It is intentionally calmer and more premium than a plain form.</div>
  <div class="card" style="left:47px;top:320px;width:305px;height:56px"><div class="fields"><div class="field">Patient name</div><div class="field">Date of birth</div><div class="field">Parent / guardian name</div><div class="field">Today's date</div></div></div>
  <div class="foot"><span>Harbourline Orthodontics | Kestrel Park | Ashgrove North | Millbrook</span><span>Page 2</span></div>
</section>

<!-- Page 3: treatment -->
<section class="page" style="left:896px;top:199px">
  <div class="band"></div>
  <div class="brand"><i></i>harbourline</div><div class="pack-label">Patient Information &amp; Consent Pack</div><div class="rule"></div>
  <div class="title-card"><div class="eyebrow">KVE consent to treatment</div><div class="title">Orthodontic Treatment</div><div class="subtitle">Overview, benefits, material risks and patient consent.</div></div>
  <div class="card bar" style="left:47px;top:120px;width:196px;height:152px;font-size:4.1px"><h4>Treatment overview</h4><p>Orthodontic treatment supports a healthy smile, healthier teeth and gums and a better bite for normal chewing. Treatment depends for much of its success on the understanding and co-operation of the patient. This form covers the usual material risks associated with orthodontic treatment. You may ask your orthodontist to explain anything you do not understand. While recognising the benefits of healthy teeth and a pleasing smile, you should also be aware that orthodontic treatment has limitations and potential risks, and there may be alternative treatment options. You should clarify what is expected of you as a patient, or as the parent of a young patient, to achieve excellent results. Keep in mind that, like other healing arts, results cannot be guaranteed. The unknown factor in any correction is the response of the patient to treatment. Should you have any questions please ask.</p></div>
  <div class="abs mark" style="left:248px;top:128px"><i></i>KVE</div>
  <div class="card bar" style="left:47px;top:283px;width:305px;height:82px;font-size:4.1px;text-align:justify"><h4>Benefits</h4><p>Orthodontics plays an important role in improving overall oral health and achieving balance and harmony between the face and teeth for a beautiful, healthy smile, which may enhance self esteem. The correct bite of teeth with healthy muscles and jaw joints will provide optimal chewing function. Properly aligned teeth are easier to brush and so the tendency to decay may be reduced, as may the likelihood of developing disease of the gums and supporting bone. Correctly aligned teeth are less likely to experience abnormal wear. Because of the individual conditions present and the limitations of treatment imposed by the nature of each benefit, not every benefit may be attainable for every patient.</p></div>
  <div class="card amber" style="left:47px;top:370px;width:305px;height:62px;font-size:4.1px;background:#fff"><h4>Risks and limitations</h4><p>All forms of medical and dental treatment, including orthodontics, have some risk and limitations. Fortunately, in orthodontics complications are infrequent and when they do occur they are usually of only minor consequence. Nevertheless, they should be considered when making the decision to undergo orthodontic treatment. The principal risks in orthodontic treatment pertain to:</p></div>
  <div class="foot"><span>Harbourline Orthodontics | Kestrel Park | Ashgrove North | Millbrook</span><span>Page 3</span></div>
</section>

<!-- Page 4: risks 01-06 -->
<section class="page" style="left:1333px;top:199px">
  <div class="band"></div>
  <div class="brand"><i></i>harbourline</div><div class="pack-label">Patient Information &amp; Consent Pack</div><div class="rule"></div>
  <div class="title-card"><div class="eyebrow">Material risks</div><div class="title">Risks to consider</div><div class="subtitle">The following risks are preserved from the KVE consent content and organized for easier reading.</div></div>
  <div class="card risk" style="left:45px;top:120px;width:148px;height:130px"><span class="num">01</span><h4>Oral Hygiene</h4><p>Orthodontic appliances do not cause tooth decay. Gum disease, tooth decay and permanent markings on teeth can occur if patients eat food containing excessive sugar or do not brush teeth frequently or properly. These same problems can occur without orthodontic treatment but the risk is greater to an individual wearing braces. It is imperative during orthodontic treatment that extra care be taken with oral hygiene and tooth brushing in particular.</p></div>
  <div class="card risk" style="left:199px;top:120px;width:148px;height:132px"><span class="num">02</span><h4>Relapse</h4><p>Teeth may have a tendency to change their positions after treatment. The long term faithful wearing of retainers should reduce this tendency. Teeth can move at any time, whether or not they have had orthodontic treatment. This is especially true during the late teen period when active growth of the facial bones is coming to an end. The most vulnerable teeth are those at the front. Throughout life, the bite can change adversely from various causes such as eruption of wisdom teeth, growth or maturational changes, mouth breathing, playing of musical instruments and other oral habits. Occasional tooth movement will be severe enough to merit further short course treatment.</p></div>
  <div class="card risk" style="left:45px;top:259px;width:148px;height:92px"><span class="num">03</span><h4>Periodontal Health</h4><p>The health of the bone and gums which support the teeth may be affected by orthodontic tooth movement if a condition already exists, and in some rare cases where a condition does not appear to exist. In general, orthodontic treatment lessens the possibility of tooth loss or gum infection due to misalignment of the teeth or jaws. Inflammation of the gums and loss of supporting bone can occur if plaque is not removed daily with good oral hygiene.</p></div>
  <div class="card risk" style="left:199px;top:259px;width:148px;height:82px"><span class="num">04</span><h4>Root Shortening</h4><p>In some patients the length of the roots of the teeth may be shortened during orthodontic treatment. Some patients are prone to this happening, some are not. It is nearly impossible to predict susceptibility. Usually this shortening does not have significant consequences, but on very rare occasions it may become a threat to the longevity of the teeth involved.</p></div>
  <div class="card risk" style="left:45px;top:358px;width:148px;height:120px"><span class="num">05</span><h4>Jaw Joints</h4><p>Occasionally patients may suffer pain or dysfunction in the jaw joints (T.M.J's). This may present as joint pain, headaches or ear problems. These problems may occur with or without orthodontic treatment. Any of the above noted symptoms should be reported to the orthodontist. Some patients are susceptible to T.M.J. problems and some are not. Numerous studies have shown that movement of the teeth during orthodontic treatment is unrelated to the onset of T.M.J problems. Just as for similar conditions in other joints, discomfort in T.M.J's can last from a few days to several weeks or longer.</p></div>
  <div class="card risk" style="left:199px;top:358px;width:148px;height:88px"><span class="num">06</span><h4>Tooth Vitality</h4><p>Sometimes a tooth may have been traumatised by a previous accident or a tooth may be decayed or have large fillings which can cause damage to the nerve of the tooth. Orthodontic tooth movement in some cases aggravates this condition and in rare instances may lead to loss of tooth vitality and discolouration of the tooth, requiring root canal treatment and other dental treatment to restore the colour of the tooth.</p></div>
  <div class="foot"><span>Harbourline Orthodontics | Kestrel Park | Ashgrove North | Millbrook</span><span>Page 4</span></div>
</section>

<!-- Page 5: risks 07-14 -->
<section class="page" style="left:1770px;top:199px">
  <div class="band"></div>
  <div class="brand"><i></i>harbourline</div><div class="pack-label">Patient Information &amp; Consent Pack</div><div class="rule"></div>
  <div class="card risk" style="left:45px;top:66px;width:148px;height:120px"><span class="num">07</span><h4>Loose appliances and discomfort</h4><p>The gums, cheeks or lips may be scratched or irritated by newly placed appliances or by loose or broken appliances or by blows to the mouth. You will be given instruction on minimising these effects. Very rarely loose orthodontic appliances may be accidentally swallowed or aspirated. You should inform your orthodontist of any unusual symptoms, broken or loose appliances, as they are noted. Usual post adjustment tenderness should be expected, and the period of tenderness varies with each patient and the procedure performed. Typical post adjustment tenderness may last 24 to 48 hours.</p></div>
  <div class="card risk" style="left:199px;top:66px;width:148px;height:105px"><span class="num">08</span><h4>Atypical Growth</h4><p>Insufficient, excessive or asymmetrical changes in the growth of the jaws may limit our ability to achieve the desired result. If growth becomes disproportionate during orthodontic management the treatment may be prolonged. Growth changes that occur after orthodontic treatment may alter the quality of treatment results and may require further orthodontic treatment. In some cases of atypical growth, the bite may change so much that oral surgery is required to achieve the best possible result.</p></div>
  <div class="card risk" style="left:45px;top:194px;width:148px;height:52px"><span class="num">09</span><h4>Headgear</h4><p>If improperly handled, headgear may cause injury to the face. Patients are warned not to wear the appliance during times of boisterous or competitive activity.</p></div>
  <div class="card risk" style="left:199px;top:194px;width:148px;height:72px"><span class="num">10</span><h4>Treatment Time</h4><p>The total time required to complete treatment may exceed the estimate. Poor co-operation in wearing the appliance or elastics the required hours per day, poor oral hygiene, broken appliances and missed appointments can lengthen the treatment time and affect the quality of the results.</p></div>
  <div class="card risk" style="left:45px;top:273px;width:148px;height:80px"><span class="num">11</span><h4>Co-operation</h4><p>Co-operation throughout treatment is your best guarantee of achieving a pleasing smile and good bite. Failure to co-operate could force the orthodontist to change the procedures and goals of your treatment. As a last resort treatment might have to be suspended. The consequences of early suspension may be worse than no treatment at all.</p></div>
  <div class="card risk" style="left:199px;top:273px;width:148px;height:82px"><span class="num">12</span><h4>Ceramic Brackets</h4><p>Where ceramic brackets have been used, there have been some reported incidents of patients experiencing bracket breakage or damage to teeth, including the wearing down of tooth enamel and flaking or fracturing of the tooth's enamel on debonding. Fractured brackets may result in remnants which may be harmful to the patient especially if they are chewed on, swallowed or aspirated.</p></div>
  <div class="card risk" style="left:45px;top:367px;width:148px;height:80px"><span class="num">13</span><h4>Complementary aesthetic dentistry</h4><p>If your teeth vary from normal in the number, size or shape of the teeth, achievement of the ideal result (for example, complete closure of excessive space) may require restorative treatment. The most common types of complementary treatment are cosmetic bonding, crown and bridge restorative dental care and periodontal therapy.</p></div>
  <div class="card risk" style="left:199px;top:367px;width:148px;height:55px"><span class="num">14</span><h4>General Health</h4><p>General medical problems can affect orthodontic treatment. You should keep your orthodontist informed of any changes to your medical health.</p></div>
  <div class="foot"><span>Harbourline Orthodontics | Kestrel Park | Ashgrove North | Millbrook</span><span>Page 5</span></div>
</section>

<!-- Page 6: consent -->
<section class="page" style="left:22px;top:932px">
  <div class="band"></div>
  <div class="brand"><i></i>harbourline</div><div class="pack-label">Patient Information &amp; Consent Pack</div><div class="rule"></div>
  <div class="title-card"><div class="eyebrow">Patient agreement</div><div class="title">Consent to Treatment</div><div class="subtitle">Please complete this section after reading the treatment information.</div></div>
  <div class="card bar" style="left:47px;top:118px;width:305px;height:58px;font-size:5px"><h4 style="font-size:5.4px">Authorization</h4><p>I hereby authorize</p><div class="field" style="margin-top:6px">Orthodontist / practice representative</div></div>
  <div class="card bar tint" style="left:47px;top:182px;width:305px;height:60px;font-size:5px"><h4 style="font-size:5.4px">Treatment consent</h4><p>to carry out orthodontic treatment and any other related procedures deemed necessary including X-rays, for the welfare and treatment of:</p><div class="field" style="margin-top:3px">Patient name</div></div>
  <div class="card tint" style="left:47px;top:255px;width:305px;height:75px"><div class="fields"><div class="field">Signature of patient or parent/guardian</div><div class="field">Date</div><div class="field">Name</div><div class="field">Relationship to patient</div><div class="field">Signature of Orthodontist</div></div></div>
  <div class="card amber" style="left:47px;top:337px;width:305px;height:34px;font-size:4.4px">Patients, parents or guardians should ask the orthodontist to explain anything they do not understand before signing.</div>
  <div class="abs" style="left:47px;top:381px;font-size:4px;color:var(--muted)">KVE Society of Orthodontists consent logo reference</div>
  <div class="abs mark" style="left:148px;top:395px"><i></i>KVE</div>
  <div class="foot"><span>Harbourline Orthodontics | Kestrel Park | Ashgrove North | Millbrook</span><span>Page 6</span></div>
</section>

<!-- Page 7: payment -->
<section class="page" style="left:459px;top:932px">
  <div class="band"></div>
  <div class="brand"><i></i>harbourline</div><div class="pack-label">Patient Information &amp; Consent Pack</div><div class="rule"></div>
  <div class="title-card"><div class="eyebrow">Payment options</div><div class="title">Payment Option Selection</div><div class="subtitle">Select a preferred payment method for orthodontic treatment fees.</div></div>
  <div class="card tint" style="left:47px;top:118px;width:314px;height:32px"><div class="field">Patient name</div></div>
  <p class="lead" style="left:47px;right:38px;top:157px">Thank you for choosing Harbourline Orthodontics. To assist with managing your treatment fees, please select your preferred payment method below. If you would prefer to pay at each scheduled appointment, please advise our reception team. Please note that appointments are generally scheduled every 6-8 weeks.</p>
  <div class="card" style="left:47px;top:202px;width:305px;height:54px;padding-left:22px;font-size:4.4px"><span class="box abs" style="left:8px;top:10px"></span><h4>Credit card direct debit</h4><p>I understand that Harbourline Orthodontics will send me a secure payment link to enter my credit card details. The card provided will be securely stored and used as my nominated payment method for future scheduled payments relating to my treatment plan.</p></div>
  <div class="card" style="left:47px;top:262px;width:305px;height:50px;padding-left:22px;font-size:4.4px"><span class="box abs" style="left:8px;top:10px"></span><h4>Monthly direct bank transfer</h4><p>I would like to pay via monthly direct bank transfer. I understand that I am responsible for ensuring monthly payments are made on time in accordance with my agreed payment arrangement.</p></div>
  <div class="card amber" style="left:47px;top:312px;width:305px;height:54px;font-size:4.3px"><h4>Important</h4><p>When making direct transfer payments, please use the patient's full name as the payment reference (for example: Jane Citizen), rather than the account holder's name. This ensures payments are correctly allocated to your treatment account.</p></div>
  <div class="card bar" style="left:47px;top:372px;width:162px;height:84px;font-size:4.4px"><h4>Patient declaration</h4><p>I have read and understood the payment options above and agree to my selected payment method.</p><div class="card tint" style="position:static;margin-top:4px;padding:3px 6px"><div class="fields"><div class="field">Signature</div><div class="field">Date</div></div></div></div>
  <div class="card bar" style="left:216px;top:372px;width:136px;height:84px"><h4>Our bank account details</h4><table class="bank"><tr><td>Account Name</td><td>Harbourline Ortho</td></tr><tr><td>Bank</td><td>Northbank</td></tr><tr><td>BSB</td><td>012 345</td></tr><tr><td>Account Number</td><td>55501234</td></tr></table></div>
  <div class="foot"><span>Harbourline Orthodontics | Kestrel Park | Ashgrove North | Millbrook</span><span>Page 7</span></div>
</section>

<!-- Page 8: retainers -->
<section class="page" style="left:896px;top:932px">
  <div class="band"></div>
  <div class="brand"><i></i>harbourline</div><div class="pack-label">Patient Information &amp; Consent Pack</div><div class="rule"></div>
  <div class="title-card"><div class="eyebrow">After treatment</div><div class="title">Our Retainer Policy</div><div class="subtitle">Retention is an important part of long-term orthodontic care.</div></div>
  <div class="card bar teal-note" style="left:47px;top:117px;width:305px;height:37px;font-size:4.4px">Wearing your retainers is the most important part of your orthodontic journey. Teeth shifting is a part of the natural ageing process, so lifetime maintenance is crucial.</div>
  <div class="card amber" style="left:47px;top:160px;width:305px;height:37px;font-size:4.3px"><h4>Policy position</h4><p>FOR THIS REASON WE DO NOT ENCOURAGE THE USE OF 'BONDED' OR 'PERMANENT' RETAINERS.</p></div>
  <p class="lead" style="left:47px;right:40px;top:203px;font-size:4.7px;line-height:1.3">Healthy teeth are not meant to be glued together, they are individual units and function independently. This is normally only done for areas of weak bone and gum or damaged teeth.<br>Instead we advocate responsible use of removable retainers to maintain your smile.<br>Permanent or bonded retainers are not actually permanent and can cause other unexpected problems after treatment is completed, such as difficulty to clean around those teeth which can cause plaque trapping and lead to localised gum and bone loss.<br>They are subject to breaking frequently, which is the reason that when bonded retainers are placed, it is recommended that you still wear a removable retainer over them anyway.<br>Bonded retainers only hold the front few teeth, whereas your orthodontic treatment involved improvements of ALL your teeth. Thus, holding the front teeth only gives the back teeth a chance to move out of alignment.<br>The retainers we provide at Harbourline Orthodontics are only worn at night and will hold ALL your teeth where they are at the end of your orthodontic treatment.<br>Even excellent retainer wear will not guarantee that the teeth will stay exactly the same forever, due to the natural ageing and bone changing process.<br>Minor alignment adjustments may be made to your retainers in the future to ensure that you remain happy with your smile.</p>
  <div class="card bar teal-note" style="left:47px;top:372px;width:305px;height:48px;font-size:4.3px"><h4>Follow-up care</h4><p>After 2 years of retainer reviews, further follow-up care may be charged at the current office visit rate. Lost or broken retainers will incur a fee for replacement or repair.</p></div>
  <div class="foot"><span>Harbourline Orthodontics | Kestrel Park | Ashgrove North | Millbrook</span><span>Page 8</span></div>
</section>

<!-- Page 9: completion -->
<section class="page" style="left:1333px;top:932px">
  <div class="band"></div>
  <div class="brand"><i></i>harbourline</div><div class="pack-label">Patient Information &amp; Consent Pack</div><div class="rule"></div>
  <div class="title-card"><div class="eyebrow">Completion</div><div class="title">Before you submit this pack</div><div class="subtitle">Check each required section and confirm all signature lines are completed.</div></div>
  <div class="abs" style="left:47px;top:120px">
    <div class="check"><span class="box"></span>Read the KVE orthodontic treatment overview, benefits and risks.</div>
    <div class="check"><span class="box"></span>Ask the orthodontist to explain anything that is unclear.</div>
    <div class="check"><span class="box"></span>Complete the consent to treatment signature section.</div>
    <div class="check"><span class="box"></span>Select one payment option and sign the payment declaration.</div>
    <div class="check"><span class="box"></span>Read and understand the retainer policy.</div>
  </div>
  <div class="card tint" style="left:47px;top:190px;width:305px;height:56px"><div class="fields"><div class="field">Patient / parent guardian signature</div><div class="field">Date</div><div class="field">Practice team member</div><div class="field">Date received</div></div></div>
  <div class="card bar" style="left:47px;top:253px;width:305px;height:62px;font-size:3.7px"><h4>Harbourline Orthodontics contact details</h4><p style="font-size:4.6px;margin:5px 0 3px">Dr Clara Wendt | Dr Marcus Hale | Dr Owen Reyes - Registered Specialist Orthodontists</p><p style="color:var(--muted);line-height:1.25">12 Example Parade, Kestrel Park VIC 3100 | T. 03 9000 0101 | E. kestrelpark@harbourline.example<br>48 Sample Road, Ashgrove North VIC 3200 | T. 03 9000 0202 | E. ashgrove@harbourline.example<br>7 Placeholder Street, Millbrook VIC 3300 | T. 03 9000 0303 | E. millbrook@harbourline.example</p></div>
  <p class="abs" style="left:47px;right:40px;top:320px;font-size:3.8px;color:var(--muted)">This design concept is intended for layout presentation. Final legal and clinical wording should be reviewed and approved by the practice before publication.</p>
  <div class="foot"><span>Harbourline Orthodontics | Kestrel Park | Ashgrove North | Millbrook</span><span>Page 9</span></div>
</section>

</div>
</body>
</html>
```